Antarctic expedition film, FROSTmere, needs a poster designed

We need a poster that will become the iconic cover for an indie, adventure film about a self-supported sea-kayaking expedition in Antarctica (both in portrait AND landscape). We then need to slightly adapt the same poster to become a poster for the roadshow (can be in either portrait OR landscape) for the release of the said film. You can read the full film synopsis at the links below but to give you a taste: "Antarctica is a place of true wilderness that few get to visit, let alone connect with. Two paddlers with adventurous spirits, whom when presented with a unique opportunity to undertake a self-supported sea kayak expedition in Antarctica, took it. They took it as an opportunity to go beyond adrenalin-based desires and instead took it as an opening to explore as much within themselves as discovering the magical, ice-choked waterways of the Antarctic Peninsula." We are looking for a clean design that embodies the purity of Antarctica yet with the notion of adventure. We're thinking a single, powerful image that captures the essence of the film and shows grandeur and space. But, perhaps combined images could be used if that seems to work better to achieve the same goal. We already have an existing font for the title (provided) and will provide some logos and a variety of pro-images from the expedition to use as needed. We also have some text that we'd like included which is provided in the uploaded file "Project Details.doc." The title font is just what we have used in the past. We are not super attached to it and if you think you can present it in a more stylised manner that better suits the poster you are putting together, please feel free to amend it.PLEASE NOTE: the entirety of the project brief is not included here - this is an overview only. PLEASE REFER to the file "Project Details.doc" provided for the complete brief.For information we have provided the following files as attachments here:- Project Details.doc- FROSTmere Overview.doc (more information about the film and the adventurers themselves)- Images from the Expedition (both to use in the design and to give a better understanding of Antarctica and the expedition itself)- Logos- Existing FROSTmere fonts- Examples we like.zip (a folder of images of a few films that we have seen that we like the look of to give you an idea of the kind of thing we're hoping for as final deliverables)Format: the final deliverables are to be used in electronic format only. Receiving them in a normal picture format and in their raw format (i.e. Illustrator etc) would be ideal.Thank you for your time!

Font styles to use
Sans Serif

Colors

Designer to choose colors to be used in the design.

Requirements
Must have
• The FROSTmere title
• An inviting image that portrays what the film is about
Nice to have
• An image/combination of images that depict vastness, wilderness, space and adventure within that wilderness

```html
<!DOCTYPE html>
<html lang="en">
<head>
<meta charset="utf-8">
<title>FROSTmere – Roadshow Poster</title>
<link rel="stylesheet" href="https://fonts.googleapis.com/css2?family=Anton&family=Fira+Sans+Condensed:wght@300;400&display=swap">
<style>
  :root {
    --page: #ffffff;
    --title-blue: #3f9fd6;
    --title-edge: #2a7fb4;
    --teal: #2f7b8a;
    --ink: #262626;
    --white: #ffffff;
    --bubble: rgba(96, 164, 188, 0.55);
  }
  html, body {
    margin: 0;
    width: 1200px;
    height: 1200px;
    overflow: hidden;
    background: var(--page);
  }
  .poster {
    position: absolute;
    left: 34px;
    top: 200px;
    width: 1131px;
    height: 800px;
    overflow: hidden;
    font-family: "Fira Sans Condensed", sans-serif;
  }
  .poster__photo {
    position: absolute;
    inset: 0;
    background:
      radial-gradient(ellipse 260px 160px at 1000px 620px, rgba(150,200,215,0.55), transparent 70%),
      linear-gradient(160deg, transparent 55%, rgba(40,48,55,0.9) 75%, rgba(30,36,42,1) 100%),
      radial-gradient(ellipse 700px 200px at 250px 760px, #eef2f5 40%, transparent 75%),
      linear-gradient(180deg, #8e9499 0%, #b9bfc4 18%, #cfd9df 30%, #b7c9d3 50%, #a7bfcc 68%, #dfe7ec 86%, #eef2f5 100%);
  }
  .poster__title {
    position: absolute;
    top: 18px;
    left: 0;
    width: 100%;
    margin: 0;
    text-align: center;
    font-family: "Anton", sans-serif;
    font-weight: 400;
    font-size: 168px;
    line-height: 1.15;
    letter-spacing: 2px;
    color: var(--title-blue);
    -webkit-text-stroke: 1px var(--title-edge);
  }
  .poster__tagline {
    position: absolute;
    top: 198px;
    left: 0;
    width: 100%;
    margin: 0;
    text-align: center;
    font-size: 38px;
    font-weight: 400;
    color: var(--teal);
    word-spacing: 4px;
    white-space: pre;
  }
  .screenings {
    position: absolute;
    left: 20px;
    top: 318px;
    margin: 0;
    padding: 0;
    list-style: none;
    font-size: 29px;
    line-height: 40px;
    color: var(--ink);
  }
  .intro-bubble {
    position: absolute;
    left: 758px;
    top: 336px;
    width: 368px;
    height: 224px;
    border-radius: 50%;
    background: var(--bubble);
    display: flex;
    align-items: center;
    justify-content: center;
    text-align: center;
    color: var(--white);
    font-size: 25px;
    line-height: 33px;
  }
  .credit {
    position: absolute;
    top: 706px;
    left: 0;
    width: 100%;
    text-align: center;
    margin: 0;
    font-size: 32px;
    font-weight: 300;
    color: var(--white);
  }
  .contact {
    position: absolute;
    top: 756px;
    font-size: 27px;
    font-weight: 300;
    line-height: 30px;
    color: var(--teal);
    display: flex;
    align-items: center;
    gap: 8px;
  }
  .contact__mark {
    display: inline-block;
    width: 20px;
    height: 20px;
    background: var(--teal);
    border-radius: 3px;
  }
  .contact--page { left: 19px; }
  .contact--photos { left: 470px; }
  .contact--web { right: 17px; color: var(--white); }
  .contact--web .contact__mark { background: var(--white); border-radius: 50%; }
</style>
</head>
<body>
  <section class="poster">
    <div class="poster__photo" role="img" aria-label="Expedition photograph: a red tent pitched in snow beneath a towering blue glacier wall, dark still water and rocks along the shore, kayaks on the beach, grey overcast sky"></div>

    <h1 class="poster__title">FROSTmere</h1>
    <p class="poster__tagline">Two people  two kayaks  two weeks</p>

    <ul class="screenings">
      <li>Hobart | Harbour Picturehouse | April 1</li>
      <li>Arrowtown | Millrace Theatre | April 3</li>
      <li>Dunedin | Kerr Hall | April 5</li>
      <li>Christchurch | Lantern Cinema | April 8</li>
      <li>Motueka | Orchard Picturehouse | April 12</li>
    </ul>

    <div class="intro-bubble">
      <p>Live intro by the 2<br>adventurers/film-makers on<br>Antarctica &amp; their expedition<br>followed by a public Q&amp;A</p>
    </div>

    <p class="credit">A Film by Harrow | Quill &amp; Driftline</p>

    <div class="contact contact--page"><span class="contact__mark"></span>@ FROSTmerefilm</div>
    <div class="contact contact--photos"><span class="contact__mark"></span>@ FROSTmere_film</div>
    <div class="contact contact--web"><span class="contact__mark"></span>frostmere-film.example</div>
  </section>
</body>
</html>
```